Voltline Assemblies, Inc. Business Card

Voltline has three operating entities and I'm looking for a standard business card template that can be used for Voltline and the three operating entities that the logo just get swapped out, but has a very similar look and feel. Ultimately if someone had a business card from each, they assume the organizations are related because they all have the same look and feel.
Below are our websites and I will attached the logos for each entity:
https://www.voltlineassemblies.example/
https://www.brantoceramic.example/
https://www.omra-kfsd.example/
https://www.summitbreaker.example/

Target Market(s)

US Voltline

Industry/Entity Type

US Voltline

Contact Information for Business Card

Normal stuff

```html
<!DOCTYPE html>
<html lang="en">
<head>
<meta charset="utf-8">
<title>Voltline Assemblies, Inc. Business Card</title>
<link href="https://fonts.googleapis.com/css2?family=Lato:wght@400;700&display=swap" rel="stylesheet">
<style>
  :root {
    --page-bg: #e9e7e4;
    --navy-deep: #161a29;
    --navy-light: #2b3149;
    --brand-red: #8c1416;
    --brand-red-dark: #5e0c0e;
    --name-red: #a8201f;
    --text-light: #dcdee5;
    --frost-top: #f1efec;
    --frost-bottom: #d9d6d2;
    --brand-ink: #1d2133;
  }
  html, body {
    margin: 0;
    width: 1200px;
    height: 970px;
    overflow: hidden;
    background: var(--page-bg);
    font-family: "Lato", sans-serif;
  }
  .business-card {
    position: absolute;
    left: 100px;
    top: 200px;
    width: 1000px;
    height: 571px;
    background: linear-gradient(180deg, var(--frost-top), var(--frost-bottom));
    box-shadow: 0 18px 40px rgba(0,0,0,0.18);
    overflow: hidden;
  }
  .card-shapes {
    position: absolute;
    inset: 0;
  }
  .contact-block {
    position: absolute;
    left: 48px;
    top: 150px;
    color: var(--text-light);
  }
  .person-name {
    margin: 0;
    font-size: 31px;
    font-weight: 400;
    color: var(--name-red);
    line-height: 1.1;
  }
  .person-title {
    margin: 4px 0 0;
    font-size: 21px;
    line-height: 1.2;
  }
  .address {
    margin: 26px 0 0;
    font-size: 22px;
    line-height: 28px;
    font-style: normal;
  }
  .contact-list {
    list-style: none;
    margin: 10px 0 0;
    padding: 0;
    font-size: 22px;
  }
  .contact-list li {
    display: flex;
    align-items: center;
    height: 29px;
  }
  .contact-icon {
    width: 16px;
    height: 16px;
    margin-right: 16px;
    flex: none;
  }
  .brand-lockup {
    position: absolute;
    left: 590px;
    top: 262px;
    display: flex;
    align-items: center;
  }
  .brand-dot {
    width: 50px;
    height: 50px;
    border-radius: 50%;
    background: var(--brand-ink);
    margin-right: 14px;
  }
  .brand-name {
    font-size: 23px;
    font-weight: 700;
    color: var(--brand-ink);
    white-space: nowrap;
  }
</style>
</head>
<body>
  <div class="business-card">
    <svg class="card-shapes" viewBox="0 0 1000 571" width="1000" height="571" aria-hidden="true">
      <defs>
        <linearGradient id="navyPanel" x1="0" y1="0" x2="1" y2="1">
          <stop offset="0" stop-color="#2b3149"/>
          <stop offset="0.55" stop-color="#1d2235"/>
          <stop offset="1" stop-color="#161a29"/>
        </linearGradient>
        <linearGradient id="redBolt" x1="0" y1="0" x2="0" y2="1">
          <stop offset="0" stop-color="#5e0c0e"/>
          <stop offset="0.5" stop-color="#8c1416"/>
          <stop offset="1" stop-color="#6e1012"/>
        </linearGradient>
      </defs>
      <polygon class="navy-panel" fill="url(#navyPanel)" points="0,0 491,0 491,389 442,389 439,571 0,571"/>
      <polygon class="red-bolt" fill="url(#redBolt)" points="491,0 498,0 531,571 439,571 442,389 491,389"/>
      <polyline class="bolt-edge" fill="none" stroke="#cfcfd4" stroke-width="1.2" points="491,0 491,389 442,389 439,571"/>
    </svg>

    <div class="contact-block">
      <h1 class="person-name">Daniel Harlow</h1>
      <p class="person-title">President</p>
      <address class="address">4120 Birchwood Court<br>Fairbanks, Alaska 99701</address>
      <ul class="contact-list">
        <li>
          <svg class="contact-icon" viewBox="0 0 16 16"><path fill="#a8201f" d="M3.2 1.2l2.4 2.6-1.2 1.8c.9 2 2.6 3.7 4.6 4.6l1.8-1.2 2.6 2.4-1.4 2.4C6.9 13.6 2.4 9.1 1 3z"/></svg>
          555-214-0386
        </li>
        <li>
          <svg class="contact-icon" viewBox="0 0 16 16"><rect x="4" y="1" width="8" height="14" rx="1.5" fill="none" stroke="#a8201f" stroke-width="1.6"/><rect x="7" y="12" width="2" height="1.4" fill="#a8201f"/></svg>
          555-318-2764
        </li>
        <li>
          <svg class="contact-icon" viewBox="0 0 16 16"><rect x="1.5" y="4" width="13" height="9" fill="#a8201f"/><polyline points="1.5,4 8,9 14.5,4" fill="none" stroke="#1d2235" stroke-width="1.2"/></svg>
          info@voltlineassemblies.example
        </li>
        <li>
          <svg class="contact-icon" viewBox="0 0 16 16"><circle cx="8" cy="8" r="6.5" fill="#a8201f"/><path d="M1.5 8h13M8 1.5c-2.5 3-2.5 10 0 13M8 1.5c2.5 3 2.5 10 0 13" fill="none" stroke="#1d2235" stroke-width="1"/></svg>
          voltlineassemblies.example
        </li>
      </ul>
    </div>

    <div class="brand-lockup">
      <span class="brand-dot"></span>
      <span class="brand-name">Voltline Assemblies, Inc.</span>
    </div>
  </div>
</body>
</html>
```